Postcard Design

We need a postcard designed for an existing dental office in the community we are serving to mail out to the community to solicit new patients. We have an existing logo and website that we need our product designed around. We want the brochure to cater to families seeking a new dental office and need it to look upscale. Want the essentials to stand out. Our name, location, office hours and that we accept most insurances, and are always welcoming new pt. We want patients to know we have early morning "before work" hours to accommodate their schedules and for their convenience. They can always see the hygenist they choose and since we are a doctor owned and operated office, they will not be bounced from one doctor to another so they receive consistent care. To assist you , I am providing our website address. The address is larkbrookdentalcare.example
Thank you!
Updates

Sent this feedback to one individual but I thought I would send to all as I know alot are looking to our website for direction. Alot of these are really looking great. Some feedback.... probably best to say "teeth whitening" only on mailer as we no longer use GLINT(even though our website still says we do. Sorry.) That way if we change whitening systems, mailer is still accurate. Also perhaps emphasize that we have convenient early morning "before work" hours and/or perhaps to highlight and put in the Straytrue logo instead of just in small print. Also I would not post that we are closed for lunch. We can let people know when they call. Keep up the good work everyone. You guys are great and have not come across one yet I have not liked. The key is to think like a patient. What would catch your eye if you were looking for a new dentist. Important to remember that people probably get a lot of these mailers every week. I know I get several to my house at least every few weeks. What will make ours stand out? Thank you everyone for all the hard work...Regards.

Project Deadline Extended
Reason: I am hoping to get more submissions as many respondents were not able to meet the deadline. We have also changed this to a committed payment project.

Hey everyone. In efforts to get more design options to choose from I have increased the first place budget by another $100.00! I have also increased the project deadline our another 5 days. Thanks guys!!

Industry/Entity Type

Dental

```html
<!DOCTYPE html>
<html lang="en">
<head>
<meta charset="utf-8">
<title>Larkbrook Family Dental Care – Postcard</title>
<link href="https://fonts.googleapis.com/css2?family=Open+Sans:wght@400;600;700&display=swap" rel="stylesheet">
<style>
  :root {
    --page: #eceff1;
    --card-top: #ffffff;
    --card-bottom: #dceef6;
    --teal: #1fb3ad;
    --teal-light: #7fd0d2;
    --teal-pale: #c9ecee;
    --ink: #1d1d1d;
    --ink-soft: #3c3c3c;
    --rule: #b9bfc3;
    --photo-a: #e9eef2;
    --photo-b: #c9b7a4;
    --photo-c: #6a9fc0;
  }
  * { box-sizing: border-box; margin: 0; padding: 0; }
  html, body { width: 875px; height: 1200px; overflow: hidden; }
  body {
    background: var(--page);
    font-family: "Open Sans", Arial, sans-serif;
    color: var(--ink);
    position: relative;
  }
  .card {
    position: absolute;
    width: 674px;
    height: 520px;
    background: linear-gradient(180deg, var(--card-top), var(--card-bottom));
    box-shadow: 0 4px 12px rgba(0,0,0,.25);
    overflow: hidden;
  }
  .card--front { left: 58px; top: 45px; }
  .card--back  { left: 155px; top: 632px; }
  .card svg.waves { position: absolute; inset: 0; width: 674px; height: 520px; }

  .brand {
    position: absolute;
    display: flex;
    align-items: center;
    gap: 8px;
    font-size: 21px;
    font-weight: 600;
    color: var(--ink-soft);
    line-height: 1.1;
  }
  .brand__dot { width: 26px; height: 26px; border-radius: 50%; background: var(--teal); flex: none; }
  .card--front .brand { left: 22px; top: 30px; width: 250px; }
  .card--back  .brand { left: 68px; top: 62px; width: 250px; }

  .headline { position: absolute; font-size: 15px; font-weight: 400; letter-spacing: .2px; white-space: nowrap; }
  .card--front .headline { left: 322px; top: 26px; }
  .card--back  .headline { left: 30px; top: 155px; }

  .photo {
    position: absolute;
    left: 0; top: 40px; width: 674px; height: 400px;
    background: radial-gradient(ellipse at 55% 60%, var(--photo-b) 0%, var(--photo-c) 35%, var(--photo-a) 70%);
  }

  .hours-front { position: absolute; left: 34px; top: 456px; }
  .hours-front__label { font-size: 11px; margin-left: 22px; }
  .hours-front__time { font-size: 17px; margin-top: 6px; }

  .contact-front { position: absolute; right: 18px; top: 406px; text-align: left; }
  .contact-front__cta { font-size: 15px; }
  .contact-front__phone { display: flex; align-items: center; gap: 8px; font-size: 24px; font-weight: 700; margin-top: 4px; }
  .contact-front__email { font-size: 14px; color: var(--teal); margin-top: 10px; }

  .practice { position: absolute; left: 30px; top: 196px; font-size: 11.5px; line-height: 1.45; color: var(--ink-soft); }
  .practice__doctor { font-size: 13px; font-weight: 600; color: var(--teal); padding-bottom: 4px; border-bottom: 1px solid var(--rule); width: 120px; margin-bottom: 10px; }
  .practice__block { margin-bottom: 8px; }
  .practice__hours-title { color: var(--teal); }
  .insurance { position: absolute; left: 93px; top: 386px; font-size: 14px; color: var(--ink-soft); }

  .stamp { position: absolute; left: 530px; top: 72px; width: 101px; height: 85px; border: 1px solid var(--rule); }
  .address-line { position: absolute; left: 400px; width: 238px; border-top: 1px solid var(--rule); }

  .website { position: absolute; right: 24px; bottom: 14px; font-size: 17px; color: var(--ink); }
</style>
</head>
<body>

<section class="card card--front">
  <div class="photo" role="img" aria-label="Photo of a smiling family, two parents with a young girl and boy playing on their backs"></div>
  <svg class="waves" viewBox="0 0 674 520" aria-hidden="true">
    <defs>
      <linearGradient id="frontBase" x1="0" y1="0" x2="0" y2="1">
        <stop offset="0" stop-color="#ffffff"/><stop offset="1" stop-color="#dceef6"/>
      </linearGradient>
    </defs>
    <path d="M0 0 H674 V40 C560 48 470 72 370 84 C250 98 120 104 0 86 Z" fill="url(#frontBase)"/>
    <path d="M250 94 C400 86 540 62 674 38 V66 C560 74 430 92 250 94 Z" fill="var(--teal-light)"/>
    <path d="M0 326 C120 380 260 414 400 416 C520 418 620 402 674 392 V520 H0 Z" fill="var(--teal)"/>
    <path d="M0 352 C140 404 290 430 430 428 C540 426 630 410 674 402 V520 H0 Z" fill="var(--teal-pale)"/>
    <path d="M0 388 C150 430 320 452 470 444 C570 438 640 424 674 416 V520 H0 Z" fill="url(#frontBase)"/>
  </svg>

  <div class="brand"><span class="brand__dot"></span>Larkbrook Family Dental Care</div>
  <p class="headline">WE ALWAYS ARE WELCOMING NEW PATEINTS</p>

  <div class="hours-front">
    <p class="hours-front__label">Early Morning "Before Work" Hours</p>
    <p class="hours-front__time">Monday-Thursday 7AM-5PM.</p>
  </div>

  <div class="contact-front">
    <p class="contact-front__cta">call us to for free appointment:</p>
    <p class="contact-front__phone">
      <svg width="34" height="30" viewBox="0 0 34 30" aria-hidden="true">
        <path d="M2 10 C2 3 32 3 32 10 L28 13 L23 10 L23 7 C19 6 15 6 11 7 L11 10 L6 13 Z" fill="var(--ink)"/>
        <path d="M9 14 H25 L29 27 H5 Z" fill="var(--ink)"/>
        <circle cx="17" cy="20" r="4" fill="#fff"/>
      </svg>
      555 014 2290
    </p>
    <p class="contact-front__email">larkbrookdental@mail.example</p>
  </div>
</section>

<section class="card card--back">
  <svg class="waves" viewBox="0 0 674 520" aria-hidden="true">
    <path d="M0 0 H674 V28 C520 22 360 30 200 44 C120 50 50 52 0 48 Z" fill="var(--teal)"/>
    <path d="M210 54 C380 40 540 34 674 40 V56 C540 50 380 52 210 54 Z" fill="var(--teal-light)"/>
    <path d="M0 400 C140 440 300 452 450 442 C560 434 630 420 674 410 V520 H0 Z" fill="var(--teal)"/>
    <path d="M0 424 C160 462 330 470 480 458 C580 450 640 438 674 430 V520 H0 Z" fill="var(--teal-light)"/>
  </svg>

  <div class="brand"><span class="brand__dot"></span>Larkbrook Family Dental Care</div>
  <p class="headline">WE ALWAYS ARE WELCOMING NEW PATEINTS</p>

  <div class="stamp"></div>
  <div class="address-line" style="top:203px"></div>
  <div class="address-line" style="top:239px"></div>
  <div class="address-line" style="top:275px"></div>
  <div class="address-line" style="top:311px"></div>

  <div class="practice">
    <p class="practice__doctor">Nolan R. Avery, DMD</p>
    <p class="practice__block">48 W. Fernhill Ave.<br>Cedarport, FL 33999</p>
    <p class="practice__block">Phone (555) 014-2290<br>Fax (555) 014-2291</p>
    <p class="practice__hours-title">Office Hours:</p>
    <p>MON -THU&nbsp;&nbsp; 7:00 am - 4:00 pm<br>Closed (Lunch) 12:00 pm - 1:00 pm</p>
  </div>

  <p class="insurance">We take most insurances!</p>
  <p class="website">www.larkbrookdentalcare.example</p>
</section>

</body>
</html>
```